Silverleaf Rise Accounting Program

size of ad Full: 7” x 9.6”
1- this is for a ladies program so it should appeal to women.
2-however, I do not want any pictures of people in this ad.
3-all the text should be seen and not covered over by graphics.
4-It should be an ad that will draw people's attention and people should look at it and say it looks nice I want to see that ad.
5-I have put all the instructions in yellow in the file below.
6-please leave 1 inch for the footer .
good luck with this project

• no picture or vector of people.

```html
<!DOCTYPE html>
<html lang="en">
<head>
<meta charset="utf-8">
<title>Silverleaf Rise Accounting Program</title>
<link href="https://fonts.googleapis.com/css2?family=Yellowtail&family=Playfair+Display:wght@700&family=Open+Sans:wght@400;700;800&display=swap" rel="stylesheet">
<style>
  :root {
    --frame: #b9a9d1;
    --lavender: #e3d9eb;
    --purple: #6a3d8f;
    --ink-blue: #2f2a85;
    --grey: #555259;
    --highlight: #fbf67d;
    --white: #ffffff;
  }
  * { margin: 0; padding: 0; box-sizing: border-box; }
  html, body { width: 883px; height: 1200px; overflow: hidden; background: var(--white); }
  .ad {
    position: relative; width: 883px; height: 1200px; overflow: hidden;
    font-family: "Open Sans", sans-serif; color: var(--purple);
  }
  .frame {
    position: absolute; left: 13px; top: 13px; width: 857px; height: 1179px;
    border: 7px solid var(--frame);
  }
  .footer-band {
    position: absolute; left: 20px; top: 1064px; width: 843px; height: 121px;
    background: var(--lavender);
  }
  .figure-area {
    position: absolute; left: 662px; top: 20px; width: 201px; height: 1044px;
    background: linear-gradient(90deg, rgba(227,217,235,0.35), var(--lavender) 35%);
    border-radius: 80px 0 0 0;
  }
  .headline { position: absolute; left: 86px; top: 86px; }
  .headline .marker {
    position: absolute; left: 0; top: 4px; width: 420px; height: 52px;
    background: var(--highlight);
    border: 1px solid #f2ea55;
  }
  .headline h1 {
    position: relative; font-family: "Yellowtail", cursive; font-weight: 400;
    font-size: 64px; line-height: 1; padding-left: 30px; color: var(--purple);
    top: -6px; white-space: nowrap;
  }
  .serif {
    font-family: "Playfair Display", serif; font-weight: 700;
    font-variant-numeric: lining-nums;
  }
  .subhead {
    position: absolute; left: 99px; top: 182px; font-size: 33px; line-height: 44px;
    letter-spacing: -1.5px; white-space: nowrap;
  }
  .rule {
    position: absolute; left: 102px; top: 234px; width: 551px; height: 2px;
    background: linear-gradient(90deg, rgba(60,55,150,0.15), #3a3596 50%, rgba(60,55,150,0.15));
  }
  .benefits { position: absolute; left: 104px; top: 246px; list-style: none; letter-spacing: -1px; }
  .benefits li { position: relative; padding-left: 28px; white-space: nowrap; }
  .benefits li svg { position: absolute; left: 0; width: 20px; height: 20px; }
  .benefits .big { font-size: 37px; line-height: 48px; }
  .benefits .big svg { top: 17px; }
  .benefits .mid { font-size: 29px; line-height: 35px; }
  .benefits .mid svg { top: 10px; width: 18px; height: 18px; }
  .gap-sm { margin-top: 14px; }
  .gap-xs { margin-top: 8px; }
  .info {
    position: absolute; left: 104px; top: 613px; width: 581px; height: 248px;
    background: var(--lavender); border-radius: 32px; text-align: center;
  }
  .info .note { margin-top: 14px; font-size: 23px; line-height: 32px; color: var(--grey); }
  .info .event { margin-top: 6px; font-size: 40px; line-height: 42px; color: var(--ink-blue); letter-spacing: -1px; }
  .info .ask { margin-top: 10px; font-size: 19px; line-height: 24px; color: #222; }
  .info .contact { font-size: 21px; line-height: 30px; font-weight: 700; color: var(--purple); }
  .ranking {
    position: absolute; left: 104px; top: 882px; width: 315px; height: 171px;
    background: var(--lavender); border-radius: 16px;
  }
  .ranking .badge {
    position: absolute; left: 24px; top: 14px; width: 108px; height: 140px;
    border-radius: 12px; background: linear-gradient(160deg, #f6b22a, #ec7f1d);
  }
  .ranking .divider {
    position: absolute; left: 146px; top: 10px; width: 2px; height: 151px;
    background: linear-gradient(180deg, rgba(58,53,150,0.1), #3a3596, rgba(58,53,150,0.1));
  }
  .ranking p {
    position: absolute; left: 161px; top: 14px; width: 154px; white-space: nowrap;
    font-size: 16px; line-height: 20.4px; color: #1e1e1e;
  }
  .burst { position: absolute; left: 468px; top: 836px; width: 240px; height: 240px; }
  .burst-text {
    position: absolute; left: 468px; top: 906px; width: 240px; text-align: center;
    font-weight: 800; font-size: 32px; line-height: 31px; color: var(--purple);
  }
</style>
</head>
<body>
<div class="ad">
  <div class="figure-area" role="img" aria-label="Soft lavender silhouette of a professional woman holding a folder"></div>
  <div class="footer-band"></div>
  <div class="frame"></div>

  <div class="headline">
    <div class="marker"></div>
    <h1>Attention Women:</h1>
  </div>

  <h2 class="subhead serif">The Brightway Job Placement advantage</h2>
  <div class="rule"></div>

  <ul class="benefits serif">
    <li class="big"><svg viewBox="0 0 20 20"><circle cx="10" cy="10" r="8.5" fill="none" stroke="var(--purple)" stroke-width="1.6"/><path d="M6 10.2l2.8 2.8L14.2 7.4" fill="none" stroke="var(--purple)" stroke-width="1.8"/></svg>96% Placement Rate -</li>
    <li class="big"><svg viewBox="0 0 20 20"><circle cx="10" cy="10" r="8.5" fill="none" stroke="var(--purple)" stroke-width="1.6"/><path d="M6 10.2l2.8 2.8L14.2 7.4" fill="none" stroke="var(--purple)" stroke-width="1.8"/></svg>6 placement directors -</li>
    <li class="big"><svg viewBox="0 0 20 20"><circle cx="10" cy="10" r="8.5" fill="none" stroke="var(--purple)" stroke-width="1.6"/><path d="M6 10.2l2.8 2.8L14.2 7.4" fill="none" stroke="var(--purple)" stroke-width="1.8"/></svg>decades of relationships with<br>100’s of firms</li>
    <li class="mid gap-sm"><svg viewBox="0 0 20 20"><circle cx="10" cy="10" r="8.5" fill="none" stroke="var(--purple)" stroke-width="1.6"/><path d="M6 10.2l2.8 2.8L14.2 7.4" fill="none" stroke="var(--purple)" stroke-width="1.8"/></svg>A Master’s Degree in Accounting</li>
    <li class="mid gap-xs"><svg viewBox="0 0 20 20"><circle cx="10" cy="10" r="8.5" fill="none" stroke="var(--purple)" stroke-width="1.6"/><path d="M6 10.2l2.8 2.8L14.2 7.4" fill="none" stroke="var(--purple)" stroke-width="1.8"/></svg>A stable, lucrative career, with high-paying,<br>full / part time opportunities in<br>Private/Public companies</li>
  </ul>

  <section class="info">
    <p class="note">Graduates have been placed in top companies<br>(full/part time jobs).</p>
    <p class="event serif">Online open house<br>Sunday June 14, 2.00pm</p>
    <p class="ask">for an online &nbsp;link / conference number /information</p>
    <p class="contact">info@brightwayjobs.org &nbsp;or 555 014 2200 x 111</p>
  </section>

  <section class="ranking">
    <div class="badge"></div>
    <div class="divider"></div>
    <p>Northbrook<br>University,<br>Masters in<br>Accounting program,<br>received the highest<br>possible rating<br>in USA</p>
  </section>

  <svg class="burst" viewBox="0 0 240 240" aria-hidden="true">
    <polygon fill="none" stroke="var(--purple)" stroke-width="1.5"
      points="120,4 135,40 170,26 166,64 205,70 181,100 228,120 181,140 205,170 166,176 170,214 135,200 120,236 105,200 70,214 74,176 35,170 59,140 12,120 59,100 35,70 74,64 70,26 105,40"/>
    <polygon fill="var(--highlight)" style="filter:drop-shadow(0 4px 5px rgba(0,0,0,0.35))"
      points="154,10 150,48 190,40 176,78 232,98 186,118 228,150 180,156 190,210 148,186 126,234 108,192 70,218 72,174 18,162 54,130 6,104 58,92 44,48 88,62 100,14 124,46"/>
  </svg>
  <div class="burst-text">MASTERS<br>in<br>12 months</div>
</div>
</body>
</html>
```